smart logo for a small painting company located in rainy Vancouver Bc *

I need a logo design for business cards and vehicle signage that will cover the entire work van.
Colors: I am open minded
Its a residential/commercial painting company.
I live in the rain forest of western canada. Raincity Vancouver Bc.
I want something that makes people think of the environment as Precious.
I would like to see designs from conservative to wild and crazy.

Target Market(s)

high end residential/commercial painting

Industry/Entity Type

Painting And Decorating

Contact Information for Business Card

On the Front, Just the logo with the logo text. the card stock should have no white showing.
On the Back: Copper Kettle Painting Company
Owner:Bradley Oxhorne
Phone:604 382 1956
Email:copperkettlepaintingcompany@mailnest.example
Fully insured, Clean, Quality Service.

Logo Text

Copper Kettle Painting Company

Font styles to use
Other font styles liked:
• Axis

Colors

Designer to choose colors to be used in the design.

Requirements
Must have
• My project must have bold colors.
Nice to have
• A tree frog walking through paint and tracking it up the side of a building
• A tree frog being painted by an artist.
• A paisley tree frog.
Should not have
• A beret. This frog isn't french.

```html
<!DOCTYPE html>
<html lang="en">
<head>
<meta charset="UTF-8">
<title>Copper Kettle Painting Company – Business Cards</title>
<link rel="stylesheet" href="https://fonts.googleapis.com/css2?family=Open+Sans:wght@400;600;700&display=swap">
<style>
  :root {
    --backdrop: #2a2c30;
    --front-tint: #ffe4ea;
    --back-tint: #eaffe2;
    --brand-red: #ff003b;
    --brand-green: #2bff00;
    --ink: #0b0b0b;
  }
  * { margin: 0; padding: 0; box-sizing: border-box; }
  html, body {
    width: 1200px; height: 900px; overflow: hidden;
    background: var(--backdrop);
    font-family: "Open Sans", Arial, sans-serif;
  }
  .canvas { position: relative; width: 1200px; height: 900px; }

  .card {
    position: absolute;
    width: 560px; height: 320px;
    overflow: hidden;
    box-shadow: 0 14px 30px rgba(0,0,0,.45);
  }
  .card-front { left: 580px; top: 80px; background: var(--front-tint); }
  .card-back  { left: 60px;  top: 500px; background: var(--back-tint); }
  .card-shapes { position: absolute; inset: 0; }

  .brand-lockup {
    position: absolute;
    display: flex; flex-direction: column; align-items: center; gap: 10px;
  }
  .brand-mark {
    width: 70px; height: 70px; border-radius: 50%;
    background: var(--ink);
  }
  .brand-name {
    color: var(--ink);
    font-weight: 600;
    font-size: 12px;
    letter-spacing: .3px;
    text-transform: uppercase;
    white-space: nowrap;
  }
  .card-front .brand-lockup { left: 0; right: 0; top: 105px; }
  .card-back .brand-lockup { left: 40px; top: 50px; }

  .owner-block {
    position: absolute; left: 20px; top: 172px; width: 220px;
    text-align: right; color: var(--ink); line-height: 1.35;
  }
  .owner-name { display: block; font-weight: 700; font-size: 15px; }
  .owner-role { display: block; font-weight: 400; font-size: 11px; }
  .service-promise { display: block; font-weight: 600; font-size: 11px; margin-top: 4px; white-space: nowrap; }

  .divider-rule {
    position: absolute; left: 250px; top: 175px;
    width: 3px; height: 70px; background: var(--ink);
  }
  .contact-tab {
    position: absolute;
    height: 30px;
    background: var(--brand-green);
    border-radius: 14px 0 0 0;
    display: flex; align-items: center; gap: 8px;
    padding-left: 12px;
    color: var(--ink);
    font-weight: 700; font-size: 12px;
    white-space: nowrap;
  }
  .contact-tab svg { width: 16px; height: 16px; flex: none; }
  .tab-phone { left: 256px; top: 210px; width: 190px; }
  .tab-email { left: 150px; top: 252px; width: 390px; }
</style>
</head>
<body>
<main class="canvas">

  <section class="card card-front" aria-label="Business card front">
    <svg class="card-shapes" viewBox="0 0 560 320" preserveAspectRatio="none">
      <rect width="560" height="320" fill="var(--brand-red)"/>
      <path d="M150,0 H440 C360,90 480,200 390,320 H120 C200,230 80,110 150,0 Z" fill="var(--front-tint)"/>
    </svg>
    <div class="brand-lockup">
      <span class="brand-mark"></span>
      <span class="brand-name">Copper Kettle Painting Company</span>
    </div>
  </section>

  <section class="card card-back" aria-label="Business card back">
    <svg class="card-shapes" viewBox="0 0 560 320" preserveAspectRatio="none">
      <path d="M0,0 H200 C170,70 90,80 30,140 C15,155 5,170 0,190 Z" fill="var(--brand-green)"/>
      <path d="M560,110 C500,140 520,220 450,250 C400,272 360,290 340,320 H560 Z" fill="var(--brand-green)"/>
    </svg>
    <div class="brand-lockup">
      <span class="brand-mark"></span>
      <span class="brand-name">Copper Kettle Painting Company</span>
    </div>
    <div class="owner-block">
      <span class="owner-name">Bradley Oxhorne</span>
      <span class="owner-role">Owner</span>
      <span class="service-promise">Fully insured, Clean, Quality Service.</span>
    </div>
    <span class="divider-rule"></span>
    <div class="contact-tab tab-phone">
      <svg viewBox="0 0 24 24" aria-hidden="true"><path fill="var(--ink)" d="M6.6 10.8a15 15 0 0 0 6.6 6.6l2.2-2.2a1 1 0 0 1 1-.25 11.4 11.4 0 0 0 3.6.57 1 1 0 0 1 1 1V20a1 1 0 0 1-1 1A17 17 0 0 1 3 4a1 1 0 0 1 1-1h3.5a1 1 0 0 1 1 1c0 1.25.2 2.45.57 3.57a1 1 0 0 1-.25 1z"/></svg>
      <span>604 382 1956</span>
    </div>
    <div class="contact-tab tab-email">
      <svg viewBox="0 0 24 24" aria-hidden="true"><path fill="var(--ink)" d="M2 5h20v14H2z"/><path fill="none" stroke="var(--brand-green)" stroke-width="1.6" d="M2 5l10 8 10-8"/></svg>
      <span>copperkettlepaintingcompany@mailnest.example</span>
    </div>
  </section>

</main>
</body>
</html>
```